Business card

I need a business card design for my consulting company in animal welfare for livestock. I like clean, crisp, simple.

One I imagined was double-sided:
side1: just my name and contact information
side2: silhouette of farm animals. Could be 3 (pig, cow, chicken) or all the species (pig, cow, chicken, duck, sheep, rabbit, etc) that continue the length of the card. I have attached an image of a silhouette style.

But, I am open to any concept.

Industry/Entity Type

Business

```html
<!DOCTYPE html>
<html lang="en">
<head>
<meta charset="utf-8">
<title>Wellbeing Advisory for Herd &amp; Flock Keepers – Business Card</title>
<link rel="stylesheet" href="https://fonts.googleapis.com/css2?family=Montserrat:wght@700&family=Questrial&display=swap">
<style>
  :root {
    --green: #03612b;
    --green-soft: #4f8f63;
    --white: #ffffff;
    --backdrop: #e9e6e1;
  }
  * { box-sizing: border-box; margin: 0; padding: 0; }
  html, body {
    width: 1200px; height: 1000px; overflow: hidden;
    background: var(--backdrop);
  }
  .canvas { position: relative; width: 1200px; height: 1000px; }
  .card {
    position: absolute; left: 250px; width: 700px; height: 400px;
    border-radius: 28px; overflow: hidden; background: var(--white);
    box-shadow: 0 6px 18px rgba(0,0,0,0.18);
  }
  .card--back { top: 60px; }
  .card--front { top: 540px; }

  /* Back side: title and animal row */
  .back__top {
    position: absolute; left: 0; top: 0; width: 100%; height: 150px;
    background: var(--green); color: var(--white);
    display: flex; flex-direction: column; align-items: center; justify-content: center;
    text-transform: uppercase; line-height: 1.15;
  }
  .back__title {
    font-family: "Montserrat", sans-serif; font-weight: 700; font-size: 26px; letter-spacing: 0.5px;
  }
  .back__subtitle {
    font-family: "Questrial", sans-serif; font-size: 26px; letter-spacing: 0.5px; margin-top: 2px;
  }
  .back__animals {
    position: absolute; left: 40px; right: 40px; top: 168px; height: 124px;
    border-radius: 6px;
    background: linear-gradient(90deg, var(--green) 0%, var(--green-soft) 100%);
    opacity: 0.85;
  }
  .back__bottom {
    position: absolute; left: 0; bottom: 0; width: 100%; height: 90px;
    background: var(--green);
  }

  /* Front side: name band and contacts */
  .front__band {
    position: absolute; left: 0; top: 45px; width: 100%; height: 150px;
    background: var(--green); color: var(--white);
    display: flex; flex-direction: column; align-items: center; justify-content: center;
    line-height: 1.2;
  }
  .front__name {
    font-family: "Montserrat", sans-serif; font-weight: 700; font-size: 32px;
    text-transform: uppercase; letter-spacing: 0.5px;
  }
  .front__tagline {
    font-family: "Questrial", sans-serif; font-size: 26px; margin-top: 6px;
  }
  .front__contacts {
    position: absolute; left: 0; right: 0; top: 222px;
    display: flex; flex-direction: column; align-items: center;
    color: var(--green); font-family: "Questrial", sans-serif; font-size: 27px; line-height: 1.2;
  }
  .contact { display: flex; flex-direction: column; align-items: center; }
  .contact + .contact { margin-top: 12px; }
  .contact__icon { width: 32px; height: 32px; margin-bottom: 6px; }
</style>
</head>
<body>
<main class="canvas">
  <section class="card card--back" aria-label="Card back">
    <div class="back__top">
      <span class="back__title">Wellbeing Advisory</span>
      <span class="back__subtitle">for Herd &amp; Flock Keepers</span>
    </div>
    <div class="back__animals" role="img" aria-label="Row of green farm animal silhouettes: cow, sheep, pig, rabbit, duck and chicken"></div>
    <div class="back__bottom"></div>
  </section>

  <section class="card card--front" aria-label="Card front">
    <div class="front__band">
      <h1 class="front__name">Mara Castellane</h1>
      <p class="front__tagline">Wellbeing Advisory for Herd &amp; Flock Keepers</p>
    </div>
    <div class="front__contacts">
      <div class="contact">
        <svg class="contact__icon" viewBox="0 0 32 32" aria-hidden="true">
          <circle cx="16" cy="16" r="15" fill="var(--green)"/>
          <circle cx="16" cy="16" r="12.5" fill="none" stroke="var(--white)" stroke-width="1.2"/>
          <rect x="11.5" y="8" width="9" height="16" rx="1.5" fill="var(--white)"/>
          <rect x="13" y="10" width="6" height="5" fill="var(--green)"/>
          <rect x="13" y="17" width="6" height="5" fill="var(--green)" opacity="0.6"/>
        </svg>
        <span>+1.555.014.2286</span>
      </div>
      <div class="contact">
        <svg class="contact__icon" viewBox="0 0 32 32" aria-hidden="true">
          <circle cx="16" cy="16" r="15" fill="var(--green)"/>
          <circle cx="16" cy="16" r="12.5" fill="none" stroke="var(--white)" stroke-width="1.2"/>
          <rect x="8.5" y="11" width="15" height="10.5" fill="var(--white)"/>
          <path d="M8.5 11 L16 17 L23.5 11" fill="none" stroke="var(--green)" stroke-width="1.4"/>
        </svg>
        <span>mara.castellane@mailbox.com</span>
      </div>
    </div>
  </section>
</main>
</body>
</html>
```